Florida-based Coastal Landscaping Comapny Needs Postcard Designs

We are a newly established Florida-based, coastal landscaping company that is looking for some really innovative postcards that we can use to get our name our to affluent consumers that live on the coast of Florida (think on the beach) and small to medium sized businesses in the same area. We will be sending out 100s of thousands of these, so need a great design

Target Market(s)

Affluent consumers and small to medium sized businesses

Industry/Entity Type

Landscaping

Font styles to use
Sans Serif

Colors

Designer to choose colors to be used in the design.

Requirements
Must have
• Florida - looking, island looking / paradise, but incorporate landscaping themes
• Need to say something about "Enjoy your yard this summer" or something relating to summer, landscapes and florida
• and would like to make two offers $50.00 off with signing up for one of our routine maintenance programs, or 1 free landscape inspection
Should not have
• Regular generic lawn company designs. We are a top tier landscape design / build plus maintenance firm, so not your mom and pop lawn mowing company

```html
<!DOCTYPE html>
<html lang="en">
<head>
<meta charset="utf-8">
<title>Tidegrove Landscaping Postcard</title>
<link rel="stylesheet" href="https://fonts.googleapis.com/css2?family=Oswald:wght@400;500;600&family=Source+Sans+3:wght@400;600&display=swap">
<style>
  :root {
    --ink: #111111;
    --white: #ffffff;
    --card-line: #bdbdbd;
    --label-grey: #b3b3b3;
    --sky-panel: #b3e2f7;
    --offer-green: #22b24c;
    --brand-teal: #1a9fd0;
    --leaf-dark: #3f8a1f;
    --leaf-light: #9ccc3e;
  }
  * { box-sizing: border-box; margin: 0; padding: 0; }
  html, body {
    width: 766px; height: 1200px; overflow: hidden;
    background: var(--white);
    font-family: "Source Sans 3", Arial, sans-serif;
  }
  .canvas { position: relative; width: 766px; height: 1200px; }

  /* ---------- front ---------- */
  .front-card {
    position: absolute; left: 36px; top: 38px; width: 692px; height: 537px;
    border: 1px solid var(--card-line); background: var(--white);
  }
  .photo-collage { position: absolute; left: 16px; top: 17px; width: 659px; height: 339px; }
  .headline {
    position: absolute; left: 50px; top: 42px; width: 340px;
    font-family: "Oswald", "Arial Narrow", sans-serif; color: var(--white);
    text-transform: uppercase; text-align: center; line-height: 1;
    text-shadow: 0 1px 3px rgba(0,0,0,.55);
  }
  .headline-line { display: block; margin-bottom: 4px; letter-spacing: .5px; }
  .headline .small { font-size: 21px; font-weight: 500; }
  .headline .big { font-size: 38px; font-weight: 600; }
  .brand-name {
    position: absolute; left: 0; right: 0; top: 432px; text-align: center;
    font-family: "Source Sans 3", Arial, sans-serif; font-weight: 400;
    font-size: 40px; letter-spacing: 3px; color: var(--brand-teal);
  }
  .side-label {
    position: absolute; right: 36px; font-size: 14px; color: var(--label-grey);
    font-family: "Source Sans 3", Arial, sans-serif;
  }
  .label-front { top: 579px; }
  .label-back { top: 1153px; }

  /* ---------- back ---------- */
  .back-card {
    position: absolute; left: 36px; top: 612px; width: 692px; height: 536px;
    background: linear-gradient(90deg, var(--leaf-dark), var(--leaf-light) 45%, var(--leaf-dark));
  }
  .back-inner {
    position: absolute; left: 15px; top: 15px; width: 662px; height: 506px;
    background: var(--white);
  }
  .info-panel {
    position: absolute; left: 1px; top: 0; width: 317px; height: 302px;
    background: var(--sky-panel); text-align: center; color: var(--ink);
  }
  .info-title {
    margin-top: 16px; font-family: "Oswald", "Arial Narrow", sans-serif;
    font-size: 18px; font-weight: 400; font-variant: small-caps; letter-spacing: 1px;
  }
  .services { margin: 4px 12px 0; font-size: 15.5px; line-height: 24px; }
  .butterfly-spot {
    position: absolute; left: -9px; top: 164px; width: 44px; height: 43px;
    border-radius: 50% 40% 50% 40%;
    background: radial-gradient(circle, #f6c21c, #d98d10);
  }
  .call-to-action {
    margin-top: 18px; font-family: "Oswald", "Arial Narrow", sans-serif;
    font-size: 18px; letter-spacing: .8px; line-height: 27px; text-transform: uppercase;
  }
  .phone {
    font-family: "Oswald", "Arial Narrow", sans-serif; font-size: 50px;
    font-weight: 500; line-height: 1; margin-top: 8px; letter-spacing: 1px;
  }
  .offers {
    position: absolute; left: 1px; top: 302px; width: 317px; height: 125px;
    background: var(--offer-green); color: var(--white); display: flex;
  }
  .offer { padding: 6px 10px; }
  .offer-cash { width: 192px; border-right: 2px dashed var(--white); }
  .offer-head {
    font-family: "Oswald", "Arial Narrow", sans-serif; font-size: 46px;
    font-weight: 500; line-height: 1; letter-spacing: 1px;
  }
  .offer-head sup { font-size: 20px; vertical-align: 20px; }
  .offer-text { font-size: 15.5px; line-height: 17px; margin-top: 4px; }
</style>
</head>
<body>
<div class="canvas">

  <section class="front-card">
    <svg class="photo-collage" viewBox="0 0 659 339" role="img" aria-label="Collage of three photos: manicured garden with hedges, flower beds beside a patio, and a lawn edged with blooming azaleas">
      <defs>
        <linearGradient id="garden-top" x1="0" y1="0" x2="1" y2="1">
          <stop offset="0" stop-color="#4f6e2a"/><stop offset=".6" stop-color="#6f9a34"/><stop offset="1" stop-color="#3f6a22"/>
        </linearGradient>
        <linearGradient id="patio-beds" x1="0" y1="0" x2="1" y2="0">
          <stop offset="0" stop-color="#5e7482"/><stop offset=".45" stop-color="#4d8a2d"/><stop offset=".75" stop-color="#c2185b"/><stop offset="1" stop-color="#6a9a2c"/>
        </linearGradient>
        <linearGradient id="azalea-lawn" x1="0" y1="0" x2="0" y2="1">
          <stop offset="0" stop-color="#c8345c"/><stop offset=".35" stop-color="#e7b52a"/><stop offset=".6" stop-color="#8bbf3a"/><stop offset="1" stop-color="#6fae2a"/>
        </linearGradient>
      </defs>
      <polygon points="0,0 400,0 431,166 0,166" fill="url(#garden-top)"/>
      <polygon points="0,172 428,172 452,339 0,339" fill="url(#patio-beds)"/>
      <polygon points="410,0 659,0 659,339 462,339" fill="url(#azalea-lawn)"/>
    </svg>
    <h1 class="headline">
      <span class="headline-line"><span class="small">Sit back, </span><span class="big">Relax</span></span>
      <span class="headline-line"><span class="small">and </span><span class="big">Enjoy</span><span class="small"> this summer</span></span>
      <span class="headline-line"><span class="small">at </span><span class="big">Your Yard</span></span>
    </h1>
    <div class="brand-name">TIDEGROVE</div>
  </section>
  <div class="side-label label-front">FRONT</div>

  <section class="back-card">
    <div class="back-inner">
      <div class="info-panel">
        <h2 class="info-title">Specializing in</h2>
        <p class="services">Planting &amp; landscape design • Custom Masonry • Waterfalls &amp; ponds • Rock walls / Stone walls • Retaining walls • Patios &amp; walkways • Poolscape • Driveways • Land Clearing &amp; Grading • Bobcat Service</p>
        <div class="butterfly-spot" role="img" aria-label="Small yellow butterfly illustration"></div>
        <p class="call-to-action">Call for your free design<br>consultation and estimate today</p>
        <p class="phone">000-000-0000</p>
      </div>
      <div class="offers">
        <div class="offer offer-cash">
          <div class="offer-head"><sup>$</sup>50 OFF</div>
          <p class="offer-text">with signing up for one of our routine maintenance programs</p>
        </div>
        <div class="offer offer-free">
          <div class="offer-head">FREE</div>
          <p class="offer-text">1 landscape inspection</p>
        </div>
      </div>
    </div>
  </section>
  <div class="side-label label-back">BACK</div>

</div>
</body>
</html>
```